LINGERIE WEBSHOP - Velora casa

We are looking for design and layout design for our webshop. We are company that sells lingerie and other connected textile products liki payamas and etc..
Our website will have approx 500 different products within 2 main catogories Woman/Man) and approx. 10 subcategories
Here is what we expect form design:
-Color pallete should be black and white (if you wish you can add some accent color)
-we want to leave feeling to customers of good quality products towards to luxury
-UX should be simple. Feel free to suggest layout
-frontpage layout, product list layout, product description layout, blog layout
-responsive design, compatible with smartphone

Target Market(s)

woman buying for themself, man buying for woman

Industry/Entity Type

Lingerie

Logo Text

VELORA CASA

Number of Pages Required

4 page

Font styles to use
Sans Serif
Decorative

Requirements
Must have
• simple UX
Nice to have
• difference for sexy/luxury lingerie and daily/cozy lingerie
Should not have
• cheap feel, unreliable

```html
<!DOCTYPE html>
<html lang="en">
<head>
<meta charset="utf-8">
<title>Velora casa – Women's Bras</title>
<link href="https://fonts.googleapis.com/css2?family=Lato:wght@300;400;700&family=Parisienne&display=swap" rel="stylesheet">
<style>
:root{
  --ink:#2b2b2b;
  --text:#444;
  --muted:#8a8a8a;
  --line:#e4e4e4;
  --band:#f7f7f7;
  --panel:#f3f3f3;
  --footer:#efefef;
  --bar:#8c8c8c;
  --white:#fff;
}
*{box-sizing:border-box;margin:0;padding:0}
html,body{width:1200px;height:2354px;overflow:hidden;background:var(--white)}
body{position:relative;font-family:'Lato',sans-serif;color:var(--text)}
.abs{position:absolute}
.script{font-family:'Parisienne',cursive;color:var(--ink);font-weight:400}

/* header */
.site-header{position:absolute;left:0;top:0;width:1200px;height:68px;background:var(--white);box-shadow:0 1px 3px rgba(0,0,0,.06)}
.brand{position:absolute;left:128px;top:24px;font-size:24px;letter-spacing:1px;color:var(--ink);font-weight:400}
.nav{position:absolute;top:28px;font-size:12px;color:var(--ink);text-transform:uppercase}
.nav .caret{display:inline-block;width:6px;height:6px;border-right:1px solid #999;border-bottom:1px solid #999;transform:rotate(45deg);margin-left:8px;position:relative;top:-3px}
.hicon{position:absolute;top:26px}
.cart-count{position:absolute;left:1058px;top:27px;font-size:12px;color:var(--text)}

.crumbs{position:absolute;left:0;top:68px;width:1200px;height:40px;background:var(--band)}
.crumbs p{position:absolute;left:131px;top:14px;font-size:11px;color:var(--text);letter-spacing:.3px}

.page-title{position:absolute;left:0;width:1488px;top:134px;text-align:center;font-size:30px;letter-spacing:1px}

/* sidebar */
.filters{position:absolute;left:128px;top:196px;width:256px;height:640px;background:var(--panel)}
.filters h2{position:absolute;left:15px;top:24px;font-size:17px;font-weight:400;letter-spacing:2.5px;color:var(--ink)}
.filter-panel{position:absolute;left:7px;top:82px;width:241px;height:505px;background:var(--white)}
.filter-row{position:absolute;left:0;width:241px;height:43px;border-bottom:1px solid var(--line);font-size:13px;color:var(--ink);padding:15px 0 0 8px}
.filter-row .caret{position:absolute;right:12px;top:18px;width:6px;height:6px;border-right:1px solid #777;border-bottom:1px solid #777;transform:rotate(45deg)}
.cat{position:absolute;font-size:12.5px;color:var(--ink)}
.cat.sub{font-size:11.5px;color:#555}
.cat.top{font-size:13px}
.cat.active{text-decoration:underline}

/* listing */
.count{position:absolute;left:416px;top:212px;font-size:12px;color:var(--muted)}
.sort{position:absolute;left:880px;top:196px;width:192px;height:42px;border:1px solid var(--line);font-size:12px;color:var(--ink);padding:15px 0 0 14px}
.sort .caret{position:absolute;right:16px;top:17px;width:6px;height:6px;border-right:1px solid #777;border-bottom:1px solid #777;transform:rotate(45deg)}

.grid{position:absolute;left:416px;top:278px;display:grid;grid-template-columns:repeat(4,152px);column-gap:16px;row-gap:113px}
.card{width:152px;height:160px;position:relative}
.card .photo{width:152px;height:160px}
.card .name{position:absolute;left:0;top:174px;width:152px;text-align:center;font-size:13px;color:var(--muted);font-weight:400}
.card .price{position:absolute;left:0;top:196px;width:152px;text-align:center;font-size:13px;color:var(--ink);letter-spacing:.3px}
.card .price.lg{font-size:15px;top:194px}
.card.hover .photo{outline:1px solid #bbb}
.hover .heart{position:absolute;right:8px;top:8px}
.swatches{position:absolute;left:32px;top:104px;display:flex;gap:8px}
.swatches span{width:15px;height:15px;border-radius:50%;display:block}
.sizes{position:absolute;left:0;top:140px;width:152px;height:20px;background:rgba(255,255,255,.75);font-size:9px;color:#555;display:flex;justify-content:center;gap:14px;padding-top:5px}

/* pagination */
.pager{position:absolute;top:1914px;display:flex;left:692px;gap:8px}
.pager span{width:24px;height:24px;font-size:12px;text-align:center;line-height:24px;background:#eee;color:var(--ink)}
.pager span.current{background:#555;color:var(--white)}
.pager .next{background:none;color:#999}

/* footer */
.site-footer{position:absolute;left:0;top:2011px;width:1200px;height:313px;background:var(--footer)}
.footer-brand{position:absolute;left:160px;top:108px;font-size:23px;letter-spacing:1px;color:var(--ink)}
.social{position:absolute;left:203px;top:157px;display:flex;gap:14px}
.social span{width:11px;height:11px;border-radius:50%;background:#555;display:block}
.footer-col h3{position:absolute;font-size:22px}
.footer-link{position:absolute;font-size:13px;color:var(--ink);letter-spacing:.2px}
.contact-line{position:absolute;left:921px;font-size:13px;color:var(--ink);line-height:19px}
.cicon{position:absolute;left:896px}
.bottom-bar{position:absolute;left:0;top:2324px;width:1200px;height:30px;background:var(--bar)}
.bottom-bar p{position:absolute;left:128px;top:9px;font-size:11px;color:var(--white)}
.cards{position:absolute;left:813px;top:8px;display:flex;gap:5px}
.cards span{width:21px;height:14px;border-radius:2px;background:#d9d9d9;display:block}
</style>
</head>
<body>

<header class="site-header">
  <div class="brand">VELORA CASA</div>
  <nav>
    <span class="nav" style="left:369px">Front page</span>
    <span class="nav" style="left:464px">Women<i class="caret"></i></span>
    <span class="nav" style="left:547px">Men<i class="caret"></i></span>
    <span class="nav" style="left:609px">Children<i class="caret"></i></span>
    <span class="nav" style="left:700px">About us</span>
    <span class="nav" style="left:783px">Contact</span>
  </nav>
  <svg class="hicon" style="left:957px" width="16" height="16" viewBox="0 0 16 16" fill="none" stroke="#555" stroke-width="1.2"><circle cx="6.5" cy="6.5" r="5"/><path d="M10.2 10.2 15 15"/></svg>
  <svg class="hicon" style="left:997px" width="17" height="16" viewBox="0 0 17 16" fill="none" stroke="#555" stroke-width="1.2"><path d="M8.5 14.5S1.5 10 1.5 5.3A3.6 3.6 0 0 1 8.5 4a3.6 3.6 0 0 1 7 1.3C15.5 10 8.5 14.5 8.5 14.5Z"/></svg>
  <svg class="hicon" style="left:1038px" width="15" height="16" viewBox="0 0 15 16" fill="none" stroke="#555" stroke-width="1.2"><rect x="1.5" y="5" width="12" height="10" rx="1"/><path d="M4.5 5V4a3 3 0 0 1 6 0v1"/></svg>
  <span class="cart-count">(0)</span>
</header>

<div class="crumbs"><p>HOME &nbsp;/&nbsp; WOMEN &nbsp;/&nbsp; BRAS</p></div>

<h1 class="page-title script">Women's Bras</h1>

<aside class="filters">
  <h2>FILTERS</h2>
  <div class="filter-panel">
    <div class="filter-row" style="top:0">PRICE<i class="caret"></i></div>
    <div class="filter-row" style="top:42px">SIZE<i class="caret"></i></div>
    <div class="filter-row" style="top:85px">COLOUR<i class="caret"></i></div>
    <span class="cat top" style="left:8px;top:142px">WOMEN</span>
    <span class="cat" style="left:16px;top:172px">Body</span>
    <span class="cat" style="left:16px;top:200px">Knickes</span>
    <span class="cat active" style="left:16px;top:230px">Bras</span>
    <span class="cat sub" style="left:30px;top:260px">Navelle</span>
    <span class="cat sub" style="left:30px;top:283px">Corvane</span>
    <span class="cat sub" style="left:30px;top:307px">Miravel</span>
    <span class="cat sub" style="left:30px;top:331px">Ostrea</span>
    <span class="cat" style="left:16px;top:360px">Swimsuits</span>
    <span class="cat" style="left:16px;top:390px">T-Shirts</span>
    <span class="cat" style="left:16px;top:418px">Pidzame</span>
    <span class="cat" style="left:16px;top:447px">Undershirt</span>
    <span class="cat" style="left:16px;top:475px">Leggings</span>
  </div>
</aside>

<p class="count">Showing 1–24 of 49 items</p>
<div class="sort">SORT BY<i class="caret"></i></div>

<main class="grid">
  <div class="card"><div class="photo" role="img" aria-label="Black push-up bra on a white mannequin" style="background:linear-gradient(#eef1f6 35%,#1c2030 60%,#eef1f6 80%)"></div><p class="name">Gaćice Navelle 3324</p><p class="price">75.00 kn</p></div>
  <div class="card"><div class="photo" role="img" aria-label="Black lace plunge bra on a mannequin" style="background:linear-gradient(#eceef0 35%,#1a1819 62%,#eceef0 85%)"></div><p class="name">Gaćice Navelle 3324</p><p class="price">75.00 kn</p></div>
  <div class="card hover">
    <div class="photo" role="img" aria-label="White lace bra on a mannequin" style="background:linear-gradient(#e6e8ec 30%,#d2d4d8 60%,#e9eaed 85%)"></div>
    <svg class="heart" width="18" height="17" viewBox="0 0 17 16" fill="none" stroke="#555" stroke-width="1.2"><path d="M8.5 14.5S1.5 10 1.5 5.3A3.6 3.6 0 0 1 8.5 4a3.6 3.6 0 0 1 7 1.3C15.5 10 8.5 14.5 8.5 14.5Z"/></svg>
    <div class="swatches"><span style="background:#fff"></span><span style="background:#2a2a2a"></span><span style="background:#e5332f"></span><span style="background:#3d7bd6"></span></div>
    <div class="sizes"><span>S/M</span><span>S-2</span><span>L</span><span>XL</span></div>
    <p class="name">Gaćice Navelle 3324</p><p class="price">75.00 kn</p>
  </div>
  <div class="card"><div class="photo" role="img" aria-label="Black lace balconette bra on a mannequin" style="background:linear-gradient(#eceef0 30%,#1b1a1c 60%,#eceef0 85%)"></div><p class="name">Gaćice Navelle 3324</p><p class="price">75.00 kn</p></div>

  <div class="card"><div class="photo" role="img" aria-label="Burgundy floral bra and briefs set" style="background:linear-gradient(#f1eff0 5%,#9a1e3d 30%,#f1eff0 55%,#9a1e3d 85%)"></div><p class="name">Gaćice Navelle 3324</p><p class="price lg">75.00 kn</p></div>
  <div class="card"><div class="photo" role="img" aria-label="Black mesh bra and briefs set" style="background:linear-gradient(#eeeeee 5%,#6c6668 30%,#eeeeee 55%,#3a3a3a 85%)"></div><p class="name">Gaćice Navelle 3324</p><p class="price lg">75.00 kn</p></div>
  <div class="card"><div class="photo" role="img" aria-label="Black balconette bra with lace trim" style="background:linear-gradient(#eceef0 25%,#111 55%,#eceef0 85%)"></div><p class="name">Gaćice Navelle 3324</p><p class="price">75.00 kn</p></div>
  <div class="card"><div class="photo" role="img" aria-label="Dark navy padded bra on a mannequin" style="background:linear-gradient(#eef1f6 35%,#141a2a 60%,#eef1f6 85%)"></div><p class="name">Gaćice Navelle 3324</p><p class="price">75.00 kn</p></div>

  <div class="card"><div class="photo" role="img" aria-label="Black strapless bra on a mannequin" style="background:linear-gradient(#eef0f3 30%,#0d0d0f 60%,#eef0f3 85%)"></div><p class="name">Gaćice Navelle 3324</p><p class="price">75.00 kn</p></div>
  <div class="card"><div class="photo" role="img" aria-label="Black bra and briefs on a full mannequin" style="background:linear-gradient(#eef1f6 10%,#191c27 30%,#eef1f6 55%,#141414 85%)"></div><p class="name">Gaćice Navelle 3324</p><p class="price">75.00 kn</p></div>
  <div class="card"><div class="photo" role="img" aria-label="Navy half-cup bra on a mannequin" style="background:linear-gradient(#eef1f6 30%,#161b2b 58%,#eef1f6 85%)"></div><p class="name">Gaćice Navelle 3324</p><p class="price">75.00 kn</p></div>
  <div class="card"><div class="photo" role="img" aria-label="Nude beige bra with lace trim" style="background:linear-gradient(#eeeceb 25%,#e9c1ae 55%,#eeeceb 85%)"></div><p class="name">Gaćice Navelle 3324</p><p class="price">75.00 kn</p></div>

  <div class="card"><div class="photo" role="img" aria-label="Navy lace bra and briefs set" style="background:linear-gradient(#eef1f6 15%,#1e2235 35%,#eef1f6 60%,#1c1c22 88%)"></div><p class="name">Gaćice Navelle 3324</p><p class="price">75.00 kn</p></div>
  <div class="card"><div class="photo" role="img" aria-label="Black smooth bra on a mannequin" style="background:linear-gradient(#ededed 25%,#121212 55%,#ededed 85%)"></div><p class="name">Gaćice Navelle 3324</p><p class="price">75.00 kn</p></div>
  <div class="card"><div class="photo" role="img" aria-label="Indigo satin bra on a mannequin" style="background:linear-gradient(#eceef2 20%,#2b2f5c 55%,#eceef2 85%)"></div><p class="name">Gaćice Navelle 3324</p><p class="price">75.00 kn</p></div>
  <div class="card"><div class="photo" role="img" aria-label="Black lace bralette on a mannequin" style="background:linear-gradient(#ecedef 0%,#2a2828 40%,#2a2828 70%,#ecedef 100%)"></div><p class="name">Gaćice Navelle 3324</p><p class="price">75.00 kn</p></div>

  <div class="card"><div class="photo" role="img" aria-label="Mauve lace bra on a mannequin" style="background:linear-gradient(#eeeeee 25%,#8f7f80 55%,#eeeeee 85%)"></div><p class="name">Gaćice Navelle 3324</p><p class="price">75.00 kn</p></div>
  <div class="card"><div class="photo" role="img" aria-label="Black and white print bra and briefs set" style="background:linear-gradient(#eeeeee 10%,#585a5e 30%,#eeeeee 55%,#3a3a3e 85%)"></div><p class="name">Gaćice Navelle 3324</p><p class="price">75.00 kn</p></div>
  <div class="card"><div class="photo" role="img" aria-label="Ivory embroidered full-cup bra" style="background:linear-gradient(#efeeed 20%,#e3d3c8 55%,#efeeed 85%)"></div><p class="name">Gaćice Navelle 3324</p><p class="price">75.00 kn</p></div>
  <div class="card"><div class="photo" role="img" aria-label="Black moulded bra on a mannequin" style="background:linear-gradient(#eeeeee 30%,#0f0f0f 58%,#eeeeee 85%)"></div><p class="name">Gaćice Navelle 3324</p><p class="price">75.00 kn</p></div>

  <div class="card"><div class="photo" role="img" aria-label="Peach lace bralette on a mannequin" style="background:linear-gradient(#f1ece8 10%,#f0cdb9 50%,#f1ece8 95%)"></div><p class="name">Gaćice Navelle 3324</p><p class="price">75.00 kn</p></div>
  <div class="card"><div class="photo" role="img" aria-label="Cream lace strapless bra" style="background:linear-gradient(#e6e6e4 20%,#f4f1e6 55%,#e6e6e4 85%)"></div><p class="name">Gaćice Navelle 3324</p><p class="price">75.00 kn</p></div>
  <div class="card"><div class="photo" role="img" aria-label="Olive lace bra and briefs set" style="background:linear-gradient(#5a5b3c 5%,#eeeeee 40%,#eeeeee 60%,#4b4c32 85%)"></div><p class="name">Gaćice Navelle 3324</p><p class="price">75.00 kn</p></div>
  <div class="card"><div class="photo" role="img" aria-label="Blue floral lace bodysuit set" style="background:linear-gradient(#e9ecf3 0%,#3c4c9a 35%,#5061b0 70%,#e9ecf3 100%)"></div><p class="name">Gaćice Navelle 3324</p><p class="price">75.00 kn</p></div>
</main>

<div class="pager"><span class="current">1</span><span>2</span><span>3</span><span class="next">›</span></div>

<footer class="site-footer">
  <div class="footer-brand">VELORA CASA</div>
  <div class="social"><span></span><span></span><span></span><span></span></div>

  <div class="footer-col"><h3 class="script" style="left:440px;top:44px">Meet us</h3></div>
  <span class="footer-link" style="left:440px;top:99px">Terms of use</span>
  <span class="footer-link" style="left:440px;top:128px">Terms of purchase</span>
  <span class="footer-link" style="left:440px;top:156px">Security payment</span>

  <div class="footer-col"><h3 class="script" style="left:654px;top:44px">Information</h3></div>
  <span class="footer-link" style="left:654px;top:100px">Payment methods</span>
  <span class="footer-link" style="left:654px;top:129px">Delivery</span>
  <span class="footer-link" style="left:654px;top:157px">Returns and replacements</span>

  <div class="footer-col"><h3 class="script" style="left:895px;top:44px">Contact</h3></div>
  <svg class="cicon" style="top:100px" width="13" height="13" viewBox="0 0 14 14"><path fill="#555" d="M3 1l2.3 2.6-1.2 1.6a8 8 0 0 0 4.7 4.7l1.6-1.2L13 11l-1.2 2C6.5 13 1 7.5 1 2.2z"/></svg>
  <p class="contact-line" style="top:97px">Tel:<br>01 / 5830-217</p>
  <svg class="cicon" style="top:160px" width="14" height="10" viewBox="0 0 14 10"><rect width="14" height="10" fill="#555"/><path d="M0 0l7 5.5L14 0" stroke="#efefef" fill="none"/></svg>
  <p class="contact-line" style="top:155px">Mail:<br>hello@veloracasa.hr</p>
  <svg class="cicon" style="top:218px" width="13" height="13" viewBox="0 0 14 14"><circle cx="7" cy="7" r="7" fill="#555"/><path d="M7 3v4h3" stroke="#efefef" fill="none" stroke-width="1.3"/></svg>
  <p class="contact-line" style="top:213px">Working hours:<br>Mon - Sat: 09 - 21 h<br>Sun: Closed</p>
</footer>

<div class="bottom-bar">
  <p>© 2020 Velora casa. Sva prava pridržana</p>
  <div class="cards"><span></span><span></span><span></span><span></span><span></span><span></span><span></span><span></span><span></span><span></span></div>
</div>

</body>
</html>
```